依頼詳細
新しく名刺のデザインを変更したいと思っております。
会社のイメージは「ホームページ」に掲載している「黄色・オレンジ」のカラーとなります。
20代から30代のお客様がメインで、あまり不動産会社といっても固くなりすぎないような、シンプルでオシャレな感じが希望です。
白の背景、文字は黒で、お洒落に少しオレンジ(ゴロ)の色に合わせてアクセントがつくような感じをイメージしております。

他社のホームページになりますが、お洒落でシンプルなデザインが希望です。
ご参考にして下さい。https://norevasta.com/
記載項目
会社名/役職/免許/
「福島店・中崎町店」
2店舗の住所・電話番号・ファックス・ホームページURL・アドレス

※表面は「氏名」「役職」「免許」など
※営業マンが2店舗移動するため、両方のお店で利用できるよう、裏面に所在地などを入れていただければと思いいます。
希望イメージ
シンプル 複雑
単色 カラフル
暗い 明るい
日常 高級
遊び心 厳粛
未来的 伝統的
女性的 男性的
補足説明
現在利用している名刺の表面・裏面
会社のロゴになります。

一般的なデザインではなく、個性があり好みでした。

この度は、沢山のご提案をいただき誠にありがとうございました。

```html
<!DOCTYPE html>
<html lang="ja">
<head>
<meta charset="utf-8">
<title>株式会社ソラリンク 名刺</title>
<link rel="stylesheet" href="https://fonts.googleapis.com/css2?family=Noto+Sans+JP:wght@400;500;700&display=swap">
<style>
  :root {
    --accent: #f5b50a;
    --ink: #1f1f1f;
    --paper: #ffffff;
  }
  html, body {
    margin: 0;
    padding: 0;
    overflow: hidden;
    background: var(--paper);
  }
  .card {
    position: relative;
    width: 726px;
    height: 1200px;
    background: var(--paper);
    overflow: hidden;
    font-family: "Noto Sans JP", sans-serif;
    color: var(--ink);
  }
  .card__bands {
    position: absolute;
    inset: 0;
  }
  .card__text {
    position: absolute;
    margin: 0;
    white-space: nowrap;
    line-height: 1;
  }
  .company-name { left: 213px; top: 210px; font-size: 42px; font-weight: 400; letter-spacing: 1px; }
  .job-title    { left: 339px; top: 360px; font-size: 31px; font-weight: 400; }
  .person-name  { left: 372px; top: 478px; font-size: 58px; font-weight: 700; letter-spacing: 2px; }
  .person-roman { left: 448px; top: 614px; font-size: 33px; font-weight: 400; }
  .mobile-label { left: 331px; top: 760px; font-size: 35px; font-weight: 400; }
  .mobile-number{ left: 349px; top: 820px; font-size: 39px; font-weight: 400; letter-spacing: 1px; }
  .brand-name   { left: 50px;  top: 548px; font-size: 42px; font-weight: 500; color: var(--accent); }
</style>
</head>
<body>
  <div class="card">
    <svg class="card__bands" width="726" height="1200" viewBox="0 0 726 1200" aria-hidden="true">
      <path d="M0 0 H726 V52 H140 Q40 52 0 120 Z" fill="var(--accent)"/>
      <path d="M0 1200 V1090 Q40 1140 150 1142 H726 V1200 Z" fill="var(--accent)"/>
    </svg>

    <p class="card__text company-name">株式会社ソラリンク</p>
    <p class="card__text job-title">ルームアドバイザー</p>
    <p class="card__text person-name">川村&emsp;直樹</p>
    <p class="card__text person-roman">Naoki Kawamura</p>
    <p class="card__text mobile-label">Mobile</p>
    <p class="card__text mobile-number">080-4172-3690</p>

    <p class="card__text brand-name">Sora Link</p>
  </div>
</body>
</html>
```